依頼詳細
下記のチャック袋に印刷を考えております。
https://www.kumotsu-h.co.jp/shop/g/g081357-62915/
記載項目
高級志向のシンプルなデザインが希望です。
希望イメージ
シンプル 複雑
単色 カラフル
暗い 明るい
日常 高級
遊び心 厳粛
未来的 伝統的
女性的 男性的
希望する色
納品ファイル
• 高解像度JPG (.jpg)
• イラストレーター形式 (.ai)
補足説明
ペット向けオゾンについて参考サイト
https://www.blue-fern.com/media/senior/life/index04.html
商品は「歯」専門となります。
歯についた歯垢、歯石を柔らかくし除去しやすくする商品となります。
動物病院で実際に売られているので、処方箋っぽい感じのデザインでお願いします。
また、使用する色は1〜2色でお願いします。

```html
<!DOCTYPE html>
<html lang="ja">
<head>
<meta charset="utf-8">
<title>VETRA オゾンデント パッケージ</title>
<link rel="stylesheet" href="https://fonts.googleapis.com/css2?family=Noto+Sans+JP:wght@400;500;700&family=Inter:wght@500;600&display=swap">
<style>
  :root {
    --ink: #111111;
    --paper: #ffffff;
  }
  * { margin: 0; padding: 0; box-sizing: border-box; }
  html, body {
    width: 853px;
    height: 1200px;
    overflow: hidden;
    background: var(--paper);
  }
  .package {
    position: relative;
    width: 853px;
    height: 1200px;
    background: var(--paper);
    color: var(--ink);
    font-family: "Noto Sans JP", sans-serif;
  }
  .brand {
    position: absolute;
    top: 168px;
    left: 0;
    width: 100%;
    text-align: center;
  }
  .brand-mark {
    display: block;
    width: 114px;
    height: 114px;
    margin: 0 auto;
    border-radius: 50%;
    background: var(--ink);
  }
  .brand-name {
    margin-top: 40px;
    font-family: "Inter", sans-serif;
    font-weight: 600;
    font-size: 25px;
    letter-spacing: 0.06em;
    line-height: 1;
  }
  .product-name {
    margin-top: 14px;
    font-weight: 500;
    font-size: 52px;
    letter-spacing: 0.02em;
    line-height: 1.1;
  }
  .features {
    position: absolute;
    top: 676px;
    left: 420px;
    list-style: none;
  }
  .feature {
    display: flex;
    align-items: center;
    height: 36px;
    margin-bottom: 33px;
    font-size: 20px;
    font-weight: 500;
    letter-spacing: 0.03em;
  }
  .feature-dot {
    width: 20px;
    height: 22px;
    margin-right: 22px;
    flex: none;
  }
  .maker {
    position: absolute;
    top: 1060px;
    left: 0;
    width: 100%;
    text-align: center;
    font-family: "Inter", sans-serif;
    font-weight: 500;
    font-size: 26px;
    letter-spacing: 0.04em;
  }
</style>
</head>
<body>
  <main class="package">
    <header class="brand">
      <span class="brand-mark" aria-hidden="true"></span>
      <p class="brand-name">VETRA</p>
      <h1 class="product-name">オゾンデント</h1>
    </header>

    <ul class="features">
      <li class="feature">
        <svg class="feature-dot" viewBox="0 0 20 22" aria-hidden="true"><ellipse cx="10" cy="11" rx="7.5" ry="8.5" fill="none" stroke="currentColor" stroke-width="4"/></svg>
        犬猫用
      </li>
      <li class="feature">
        <svg class="feature-dot" viewBox="0 0 20 22" aria-hidden="true"><ellipse cx="10" cy="11" rx="7.5" ry="8.5" fill="none" stroke="currentColor" stroke-width="4"/></svg>
        歯石や歯垢を柔らかくして除去
      </li>
      <li class="feature">
        <svg class="feature-dot" viewBox="0 0 20 22" aria-hidden="true"><ellipse cx="10" cy="11" rx="7.5" ry="8.5" fill="none" stroke="currentColor" stroke-width="4"/></svg>
        3.5g/4本入り
      </li>
    </ul>

    <footer class="maker">CLINICAL BOTANICS</footer>
  </main>
</body>
</html>
```